Frank Frenzy Feast - Team Eating Comp

Design a fun/ vibrant/ edgy/ funny/ eye catching poster for our upcoming hotdog eating challenge. We are a grundgy whiskey/ burger bar on the Sunshine Coast. We have previously done hotdog eating comps and this year will be a hybrid model. I have attached an old tshirt design, this time more pop art in the design.

Info for the poster :
- teams of 2
- can you finish 14 hotdogs between you in 10min?
- $35 to enter (refunded if you successfully complete the challenge)
- prize if you successfully complete challenge
- 29th July 2023
- 12pm-5pm
Come down to Rusty Tobs Pelicanbay for the challenge - one day only!!

rustytobspelicanbay.example

Target Market(s)

Sunshine Coast locals. Food Competitors.

Industry/Entity Type

Bar and Restaurant

Font styles to use
Other font styles liked:
• Veneer

Colors
FFF300
FFF600
FEFA6F
FFFEC7
FFFEE8
F0912C
F2A743
F7CA91
FBE8D2
FDF5EE
EE7325
F08F49
F5BC92
FAE3D3
FDF4ED
EB3D1F
EC4F4E
F09395
F8D3D4
FCEDEE

```html
<!DOCTYPE html>
<html lang="en">
<head>
<meta charset="utf-8">
<title>Rusty Tobs – Team Hotdog Challenge</title>
<link rel="stylesheet" href="https://fonts.googleapis.com/css2?family=Anton&display=swap">
<style>
  :root {
    --yellow: #FFF300;
    --cream: #FFFEE8;
    --orange: #F0912C;
    --orange-light: #F2A743;
    --orange-deep: #EE7325;
    --red: #EB3D1F;
    --red-soft: #EC4F4E;
    --peach: #F7CA91;
    --ink: #1a1410;
    --white: #ffffff;
  }
  * { margin: 0; padding: 0; box-sizing: border-box; }
  html, body { width: 849px; height: 1200px; overflow: hidden; background: var(--white); }
  .poster {
    position: relative;
    width: 849px;
    height: 1200px;
    overflow: hidden;
    font-family: "Anton", "Impact", "Arial Narrow", sans-serif;
    color: var(--white);
    text-transform: uppercase;
  }
  .backdrop { position: absolute; inset: 0; }

  .brand {
    position: absolute;
    left: 80px; top: 58px;
    display: flex; align-items: center; gap: 14px;
    font-size: 70px;
    line-height: 1;
    letter-spacing: 2px;
    color: var(--ink);
    white-space: nowrap;
  }
  .brand-dot { width: 26px; height: 26px; border-radius: 50%; background: var(--ink); }

  .mascot {
    position: absolute;
    left: 500px; top: 28px;
    width: 295px; height: 370px;
    border-radius: 42% 50% 45% 40%;
    background: radial-gradient(circle at 45% 45%, var(--peach) 0%, var(--orange) 55%, var(--red-soft) 100%);
  }

  .teams {
    position: absolute;
    left: 112px; top: 300px;
    padding: 0 22px;
    height: 92px;
    background: var(--cream);
    border: 5px solid var(--ink);
    box-shadow: 8px 8px 0 var(--red);
    font-size: 64px;
    line-height: 82px;
    color: var(--ink);
    letter-spacing: 1px;
    white-space: nowrap;
  }

  .question {
    position: absolute;
    left: 108px; top: 412px;
    width: 345px;
    background: var(--white);
    border: 5px solid var(--ink);
    color: var(--ink);
    font-size: 36px;
    line-height: 46px;
    padding: 8px 14px;
    letter-spacing: 0.5px;
  }

  .entry-badge {
    position: absolute;
    left: 455px; top: 468px;
    width: 160px; height: 160px;
  }
  .entry-badge svg { position: absolute; inset: 0; }
  .entry-text {
    position: absolute; inset: 0;
    display: flex; flex-direction: column; align-items: center; justify-content: center;
    text-align: center;
  }
  .entry-price { font-size: 58px; line-height: 1; }
  .entry-label { font-size: 21px; line-height: 1.1; }

  .refund-note {
    position: absolute;
    left: 818px; top: 600px;
    transform: translate(-50%, -50%) rotate(90deg);
    white-space: nowrap;
    font-family: Arial, Helvetica, sans-serif;
    text-transform: none;
    font-size: 17px;
    color: var(--white);
  }

  .date {
    position: absolute;
    left: 120px; width: 480px; top: 712px;
    text-align: center;
    font-size: 66px;
    line-height: 1;
    letter-spacing: 1px;
    white-space: nowrap;
    text-shadow: 4px 4px 0 var(--ink);
  }

  .hours {
    position: absolute;
    left: 240px; top: 805px;
    width: 330px; height: 82px;
    border: 5px solid var(--ink);
    background: var(--ink);
    font-size: 58px;
    line-height: 70px;
    text-align: center;
    letter-spacing: 1px;
    white-space: nowrap;
  }

  .invite {
    position: absolute;
    left: 120px; width: 600px; top: 918px;
    text-align: center;
    font-size: 40px;
    line-height: 48px;
    letter-spacing: 0.5px;
  }

  .website {
    position: absolute;
    left: 0; width: 849px; top: 1112px;
    padding-right: 60px;
    text-align: center;
    font-size: 24px;
    letter-spacing: 3px;
  }

  .hotdog-left {
    position: absolute;
    left: -90px; top: 770px;
    width: 230px; height: 110px;
    border-radius: 60px;
    transform: rotate(-20deg);
    background: linear-gradient(180deg, var(--orange-light) 0%, var(--orange-deep) 50%, var(--orange-light) 100%);
  }
  .hotdog-right {
    position: absolute;
    left: 705px; top: 1105px;
    width: 220px; height: 110px;
    border-radius: 60px;
    transform: rotate(-15deg);
    background: linear-gradient(180deg, var(--orange-light) 0%, var(--orange-deep) 50%, var(--orange-light) 100%);
  }
</style>
</head>
<body>
<main class="poster">
  <svg class="backdrop" width="849" height="1200" viewBox="0 0 849 1200" aria-hidden="true">
    <rect width="849" height="1200" fill="var(--red)"/>
    <polygon points="0,0 780,0 720,40 650,60 600,120 560,160 470,230 430,300 300,420 240,520 150,600 90,660 0,720" fill="var(--orange)"/>
    <polygon points="0,0 740,0 680,30 620,50 570,110 520,150 440,220 400,290 270,410 210,500 120,580 60,640 0,690" fill="var(--yellow)"/>
    <polygon points="0,1010 120,960 200,1000 260,1060 320,1110 400,1140 470,1150 560,1170 640,1150 720,1100 800,1060 849,1050 849,1200 0,1200" fill="var(--orange)"/>
    <polygon points="0,1040 110,1000 190,1040 250,1090 320,1140 400,1165 480,1175 560,1190 650,1175 730,1130 800,1095 849,1085 849,1200 0,1200" fill="var(--yellow)"/>
  </svg>

  <div class="brand"><span class="brand-dot"></span><span class="brand-name">Rusty Tobs</span></div>

  <div class="mascot" role="img" aria-label="Cartoon hotdog mascot giving a thumbs up"></div>

  <div class="teams">Teams of 2</div>

  <div class="question">Can you finish 14 hotdogs between you in 10min?</div>

  <div class="entry-badge">
    <svg viewBox="0 0 160 160" width="160" height="160" aria-hidden="true">
      <polygon points="80,4 146,42 146,118 80,156 14,118 14,42" fill="var(--orange)" stroke="var(--cream)" stroke-width="4"/>
    </svg>
    <div class="entry-text">
      <span class="entry-price">$35</span>
      <span class="entry-label">to enter</span>
    </div>
  </div>

  <p class="refund-note">*refunded if you successfully complete the challenge</p>

  <div class="hotdog-left" role="img" aria-label="Illustrated hotdog with mustard"></div>

  <p class="date">29th July 2023</p>

  <div class="hours">12pm-5pm</div>

  <p class="invite">Come down to Rusty Tobs Pelicanbay for the challenge - one day only!!</p>

  <div class="hotdog-right" role="img" aria-label="Illustrated hotdog with mustard"></div>

  <p class="website">rustytobspelicanbay.example</p>
</main>
</body>
</html>
```